Complete the Kurtwell Dynamics Inc. business card as started in the attached files.

See the attached card for the starting point.

Font is attached (File #3). The "F" box is a capital F on the font set, and the "Se" box is the number 4 on the font set.

I would like to see variations of the image provided (File #2). Image provided does not have proper balance of the boxes to the following letters (i.e. "F" is in a different plane than "urtwell", and "Se" is in the plane). Create the background to match the "melting chalk" example (File #1).

Completion of the work will be source files for TWO cards. One with no title under my name, and one with the title Junior Deputy Assistant to the Regional Associate Vice President.

With thanks,

Lou

Target Market(s)

Science nerds

Industry/Entity Type

Business

Requirements
Must have
• Green colour; if the background can match the pattern of the "melting chalk" background that is fantastic.
Must use the Font attached for the logo name. See notes in the brief.

```html
<!DOCTYPE html>
<html lang="en">
<head>
<meta charset="utf-8">
<title>Kurtwell Services business card</title>
<link href="https://fonts.googleapis.com/css2?family=Comfortaa:wght@500;700&family=Fira+Sans+Condensed:wght@400;700&display=swap" rel="stylesheet">
<style>
  :root {
    --page-bg: #e9e6e1;
    --green-light: #1a8a62;
    --green-mid: #0c6a45;
    --green-dark: #06432a;
    --ink: #ffffff;
    --ink-soft: #e4f2ea;
    --card-shadow: rgba(0, 0, 0, 0.28);
  }
  * { margin: 0; padding: 0; box-sizing: border-box; }
  html, body {
    width: 1200px;
    height: 913px;
    overflow: hidden;
    background: var(--page-bg);
  }
  .canvas {
    position: relative;
    width: 1200px;
    height: 913px;
  }
  .card {
    position: absolute;
    top: 306px;
    width: 520px;
    height: 300px;
    border-radius: 4px;
    background: linear-gradient(160deg, var(--green-light) 0%, var(--green-mid) 45%, var(--green-dark) 100%);
    box-shadow: 0 10px 26px var(--card-shadow);
    overflow: hidden;
    color: var(--ink);
  }
  .card--front { left: 50px; }
  .card--back { left: 630px; }

  /* Wordmark */
  .wordmark {
    position: absolute;
    font-family: "Comfortaa", sans-serif;
    font-weight: 700;
    color: var(--ink);
    line-height: 1;
    white-space: nowrap;
  }
  .wordmark__line { display: flex; align-items: center; }
  .wordmark__square {
    width: 0.72em;
    height: 0.72em;
    border: 3px solid var(--ink);
    margin-right: 0.18em;
  }
  .card--front .wordmark {
    left: 70px;
    top: 96px;
    font-size: 56px;
  }
  .card--front .wordmark__line--second { margin-left: 1.3em; margin-top: 6px; }

  .card--back .wordmark {
    left: 22px;
    bottom: 22px;
    font-size: 34px;
    transform-origin: left bottom;
    transform: translateY(-0px) rotate(-90deg) translateY(100%);
  }
  .card--back .wordmark__line--second { margin-left: 1.3em; margin-top: 4px; }

  /* Contact block */
  .contact {
    position: absolute;
    left: 230px;
    top: 38px;
    font-family: "Comfortaa", sans-serif;
    color: var(--ink-soft);
  }
  .contact__name {
    font-family: "Fira Sans Condensed", sans-serif;
    font-weight: 700;
    font-size: 20px;
    letter-spacing: 0.02em;
    text-transform: uppercase;
    color: var(--ink);
  }
  .contact__title {
    font-family: "Fira Sans Condensed", sans-serif;
    font-weight: 400;
    font-size: 10.5px;
    margin-top: 1px;
  }
  .contact__company {
    font-family: "Fira Sans Condensed", sans-serif;
    font-weight: 700;
    font-size: 17px;
    color: var(--ink);
    margin-top: 46px;
  }
  .contact__lines {
    font-size: 13px;
    line-height: 1.45;
    margin-top: 6px;
    padding-left: 6px;
  }
  .contact__gap { height: 10px; }
</style>
</head>
<body>
<div class="canvas">

  <section class="card card--front" aria-label="Card front">
    <div class="wordmark">
      <div class="wordmark__line"><span class="wordmark__square"></span>Kurtwell</div>
      <div class="wordmark__line wordmark__line--second">Services</div>
    </div>
  </section>

  <section class="card card--back" aria-label="Card back">
    <div class="contact">
      <p class="contact__name">Lou Hartwig</p>
      <p class="contact__title">Junior Deputy Assistant to the Associate Vice President</p>
      <p class="contact__company">Kurtwell Dynamics Inc.</p>
      <div class="contact__lines">
        <p>118, 40912 Range Road 174</p>
        <p>Ashgrove, AB T3K 2P9</p>
        <div class="contact__gap"></div>
        <p>Ph: 555.014.2290</p>
        <p>lou@kurtwell.ca</p>
        <p>www.kurtwell.ca</p>
      </div>
    </div>
    <div class="wordmark">
      <div class="wordmark__line"><span class="wordmark__square"></span>Kurtwell</div>
      <div class="wordmark__line wordmark__line--second">Services</div>
    </div>
  </section>

</div>
</body>
</html>
```